Business Card Design

we specialise in supply of custom uniforms - teamwear to Schools and sporting clubs, see our website: www.harbourkitcove.com.au, our main corporate colour is black and white, with small amount of gold/yellow

Industry/Entity Type

Business

Contact Information for Business Card

Harbour Kit Cove
Travis Okafor
Ph 03 6218 5097
Mobile 0462 318 740
email: travis@harbourkitcove.com.au
www.harbourkitcove.com.au
like us on facebook

Requirements
Must have
• modern look & feel

```html
<!DOCTYPE html>
<html lang="en">
<head>
<meta charset="utf-8">
<title>Harbour Kit Cove – Business Card</title>
<link href="https://fonts.googleapis.com/css2?family=Arimo:wght@400;700&display=swap" rel="stylesheet">
<style>
  :root {
    --page: #e9e7e3;
    --card-black: #050505;
    --accent-yellow: #ffec00;
    --accent-yellow-deep: #f5d400;
    --text-white: #ffffff;
    --mark-grey-light: #55575a;
    --mark-grey-dark: #1c1d1f;
  }
  * { margin: 0; padding: 0; box-sizing: border-box; }
  html, body {
    width: 1200px; height: 1000px; overflow: hidden;
    background: var(--page);
    font-family: "Arimo", Arial, sans-serif;
  }
  .business-card {
    position: absolute; left: 100px; top: 210px;
    width: 1000px; height: 580px;
    background: var(--card-black);
    overflow: hidden;
    box-shadow: 0 12px 30px rgba(0,0,0,0.25);
  }
  .accent-swoosh { position: absolute; left: 0; top: 0; width: 1000px; height: 580px; }
  .mascot-decoration {
    position: absolute; left: 60px; top: 40px;
    width: 400px; height: 300px;
    border-radius: 48% 52% 40% 60% / 55% 45% 55% 45%;
    background: radial-gradient(ellipse at 70% 25%, var(--mark-grey-light), var(--mark-grey-dark) 75%);
    opacity: 0.8;
  }
  .holder-name {
    position: absolute; right: 70px; top: 235px;
    color: var(--text-white);
    font-weight: 700; font-size: 58px; letter-spacing: -1px;
  }
  .contact-list {
    position: absolute; right: 40px; top: 345px;
    list-style: none; text-align: right;
    color: var(--text-white); font-size: 27px; line-height: 33px;
  }
  .contact-list li { display: flex; justify-content: flex-end; align-items: center; gap: 6px; }
  .contact-list .no-icon { padding-right: 30px; }
  .contact-icon { width: 24px; height: 24px; flex: none; }
  .brand-block {
    position: absolute; left: 30px; bottom: 30px;
    display: flex; align-items: center; gap: 14px;
  }
  .brand-square { width: 92px; height: 92px; background: var(--accent-yellow); }
  .brand-name {
    color: var(--text-white); font-weight: 700; font-size: 34px;
  }
</style>
</head>
<body>
  <div class="business-card">
    <svg class="accent-swoosh" viewBox="0 0 1000 580" aria-hidden="true">
      <path d="M420 92 C 640 100, 900 140, 1000 250 L 1000 0 L 920 0 C 780 40, 600 70, 420 92 Z" fill="var(--accent-yellow)"/>
      <path d="M620 70 C 760 60, 880 40, 960 0 L 1000 0 L 1000 40 C 900 70, 760 80, 620 70 Z" fill="var(--accent-yellow-deep)" opacity="0.6"/>
    </svg>

    <div class="mascot-decoration" role="img" aria-label="Large faint grey leaping mascot silhouette decoration"></div>

    <h1 class="holder-name">Travis Okafor</h1>

    <ul class="contact-list">
      <li>03 6218 5097
        <svg class="contact-icon" viewBox="0 0 24 24" aria-hidden="true"><rect x="6" y="3" width="12" height="6" fill="none" stroke="var(--accent-yellow)" stroke-width="2"/><rect x="2" y="9" width="20" height="9" rx="2" fill="var(--accent-yellow)"/><rect x="6" y="15" width="12" height="6" fill="var(--card-black)" stroke="var(--accent-yellow)" stroke-width="2"/></svg>
      </li>
      <li>0462 318 740
        <svg class="contact-icon" viewBox="0 0 24 24" aria-hidden="true"><rect x="7" y="2" width="10" height="20" rx="2" fill="var(--accent-yellow)"/><rect x="9" y="5" width="6" height="6" fill="var(--card-black)"/></svg>
      </li>
      <li>travis@harbourkitcove.com.au
        <svg class="contact-icon" viewBox="0 0 24 24" aria-hidden="true"><rect x="2" y="5" width="20" height="14" fill="none" stroke="var(--accent-yellow)" stroke-width="2"/><path d="M2 5 L12 13 L22 5" fill="none" stroke="var(--accent-yellow)" stroke-width="2"/></svg>
      </li>
      <li class="no-icon">www.harbourkitcove.com.au</li>
    </ul>

    <div class="brand-block">
      <div class="brand-square"></div>
      <span class="brand-name">Harbour Kit Cove</span>
    </div>
  </div>
</body>
</html>
```